Design for a 4 screens mobile app: Brelluvo

The app is a compact but illustrated phone/address book...
We need a design for the 5 screens of the app (see screens attached):
a) "index" : 1 screen with 6 pictures of contact person
b) "contact list" : 1 screen, to manage (add/del/edit) the contacts of the phone/address book
c) "add contact" : 1 screen to add a contact (a picture + a phone number)
d) "update contact" : similar to "add"
e) "fields missing" : add/edit screens in "error" state
We also need the ico design + loading screen.
No specific guidelines, nor logo or whatever.
It will be a free app distributed on iOS and Androïd.
We just want to make it looking nice & very usable for end users.
B2C

```html
<!DOCTYPE html>
<html lang="en">
<head>
<meta charset="utf-8">
<title>Brelluvo – App Screens</title>
<link href="https://fonts.googleapis.com/css2?family=Open+Sans:wght@400;600&display=swap" rel="stylesheet">
<style>
  :root {
    --bg: #f1f1f3;
    --blue: #4a9fdc;
    --blue-deep: #3b93d4;
    --white: #ffffff;
    --row-alt: #f7f7f8;
    --line: #e6e6e8;
    --text: #444a50;
    --muted: #8a8f94;
    --toolbar: #e9e9eb;
    --icon-grey: #9a9ea3;
  }
  * { box-sizing: border-box; margin: 0; padding: 0; }
  html, body { width: 1200px; height: 833px; overflow: hidden; }
  body {
    background: var(--bg);
    font-family: "Open Sans", Arial, sans-serif;
    color: var(--text);
    position: relative;
  }
  .screen {
    position: absolute;
    top: 142px;
    width: 298px;
    height: 530px;
    background: var(--white);
    overflow: hidden;
  }
  .screen--index { left: 102px; }
  .screen--list { left: 456px; }
  .screen--add { left: 810px; }

  .app-bar {
    position: absolute; top: 0; left: 0; right: 0;
    height: 60px;
    background: var(--blue);
    color: var(--white);
  }
  .status-bar {
    height: 20px;
    display: flex; align-items: center; justify-content: space-between;
    padding: 0 7px;
    font-size: 10px; font-weight: 600;
    position: relative;
  }
  .status-bar__left, .status-bar__right { display: flex; align-items: center; gap: 4px; }
  .status-bar__time { position: absolute; left: 0; right: 0; text-align: center; pointer-events: none; }
  .signal { display: flex; gap: 1.5px; }
  .signal i { width: 5px; height: 5px; border-radius: 50%; background: var(--white); display: block; }
  .battery { width: 20px; height: 9px; border: 1px solid var(--white); border-radius: 2px; padding: 1px; position: relative; }
  .battery::before { content: ""; display: block; width: 66%; height: 100%; background: var(--white); }
  .battery::after { content: ""; position: absolute; right: -3px; top: 2px; width: 2px; height: 3px; background: var(--white); }

  .nav {
    height: 40px;
    display: flex; align-items: center; justify-content: center;
    position: relative;
  }
  .nav__title { font-size: 17px; font-weight: 600; }
  .nav__left, .nav__right { position: absolute; top: 50%; transform: translateY(-50%); display: flex; }
  .nav__left { left: 10px; }
  .nav__right { right: 10px; }

  /* Index */
  .portrait {
    position: absolute;
    width: 128px; height: 128px;
    border-radius: 50%;
  }
  .portrait--a { background: radial-gradient(circle at 45% 40%, #d9c2ad, #7a5a44 75%); }
  .portrait--b { background: radial-gradient(circle at 50% 45%, #e2c0a4, #5b4536 75%); }
  .portrait--c { background: linear-gradient(160deg, #8fd1ea, #c9b8b0 55%, #6f6e86); }
  .portrait--d { background: radial-gradient(circle at 45% 45%, #e8cbb2, #a99a8c 75%); }

  /* Contact list */
  .contact-row {
    position: absolute; left: 0; width: 298px; height: 65px;
    display: flex; align-items: center;
    padding-left: 14px;
    border-bottom: 1px solid var(--line);
    background: var(--white);
    font-size: 12.5px;
  }
  .contact-row:nth-of-type(even) { background: var(--row-alt); }
  .avatar {
    width: 38px; height: 38px; border-radius: 50%; flex: none;
    margin-right: 18px;
  }
  .avatar--a { background: radial-gradient(circle at 45% 40%, #d9c2ad, #7a5a44 75%); }
  .avatar--b { background: radial-gradient(circle at 50% 45%, #e2c0a4, #5b4536 75%); }
  .avatar--c { background: linear-gradient(160deg, #8fd1ea, #c9b8b0 55%, #6f6e86); }
  .avatar--d { background: radial-gradient(circle at 45% 45%, #e8cbb2, #a99a8c 75%); }
  .contact-row--swiped { padding-left: 0; }
  .row-actions {
    width: 132px; height: 100%;
    background: var(--blue);
    display: flex; align-items: center; justify-content: space-around;
    padding: 0 16px;
    margin-right: 16px;
  }

  /* Add details */
  .hero {
    position: absolute; top: 60px; left: 0; right: 0; height: 245px;
    background: var(--blue);
    overflow: hidden;
  }
  .hero__halo {
    position: absolute; width: 190px; height: 190px; border-radius: 50%;
    left: 54px; top: 18px;
    background: rgba(255,255,255,0.05);
  }
  .add-image {
    position: absolute; left: 92px; top: 56px;
    width: 114px; height: 114px; border-radius: 50%;
    border: 1.5px solid var(--white);
    display: flex; align-items: center; justify-content: center;
  }
  .add-image__label {
    position: absolute; top: 183px; left: 0; right: 0;
    text-align: center; color: var(--white); font-size: 12.5px;
  }
  .field-label {
    position: absolute; top: 342px; left: 0; right: 0;
    display: flex; align-items: center; justify-content: center; gap: 6px;
    font-size: 11.5px;
  }
  .field-input {
    position: absolute; top: 377px; left: 22px; width: 258px; height: 36px;
    border: 1px solid #c9cbce; background: #fafafa;
    display: flex; align-items: center; justify-content: center;
    font-size: 11px; color: var(--muted); letter-spacing: 0.5px;
  }
  .toolbar {
    position: absolute; bottom: 0; left: 0; right: 0; height: 42px;
    background: var(--toolbar);
    display: flex; align-items: center; justify-content: space-around;
  }
</style>
</head>
<body>

<!-- Screen: Contacts index -->
<section class="screen screen--index">
  <header class="app-bar">
    <div class="status-bar">
      <div class="status-bar__left"><span class="signal"><i></i><i></i><i></i><i></i><i></i></span><span>Quorvanet</span></div>
      <span class="status-bar__time">9:23 AM</span>
      <div class="status-bar__right">
        <svg width="8" height="8" viewBox="0 0 8 8"><path d="M7.5.5L.5 3.6l3.2.6.6 3.3z" fill="#fff"/></svg>
        <span>66%</span><span class="battery"></span>
      </div>
    </div>
    <div class="nav">
      <span class="nav__left">
        <svg width="18" height="18" viewBox="0 0 24 24"><path fill="#fff" d="M10.3 2h3.4l.5 2.6 1.7.7 2.2-1.5 2.4 2.4-1.5 2.2.7 1.7 2.6.5v3.4l-2.6.5-.7 1.7 1.5 2.2-2.4 2.4-2.2-1.5-1.7.7-.5 2.6h-3.4l-.5-2.6-1.7-.7-2.2 1.5-2.4-2.4 1.5-2.2-.7-1.7L2 13.7v-3.4l2.6-.5.7-1.7-1.5-2.2 2.4-2.4 2.2 1.5 1.7-.7zM12 8.5a3.5 3.5 0 100 7 3.5 3.5 0 000-7z"/></svg>
      </span>
      <h1 class="nav__title">Contacts</h1>
      <span class="nav__right">
        <svg width="22" height="6" viewBox="0 0 22 6"><circle cx="3" cy="3" r="2.6" fill="#fff"/><circle cx="11" cy="3" r="2.6" fill="#fff"/><circle cx="19" cy="3" r="2.6" fill="#fff"/></svg>
      </span>
    </div>
  </header>
  <div class="portrait portrait--a" style="left:10px;top:79px" role="img" aria-label="Contact photo: woman with a camera"></div>
  <div class="portrait portrait--b" style="left:154px;top:79px" role="img" aria-label="Contact photo: man in sunglasses with headphones"></div>
  <div class="portrait portrait--c" style="left:10px;top:226px" role="img" aria-label="Contact photo: group of friends"></div>
  <div class="portrait portrait--d" style="left:154px;top:226px" role="img" aria-label="Contact photo: smiling man with glasses"></div>
  <div class="portrait portrait--a" style="left:10px;top:373px" role="img" aria-label="Contact photo: woman with a camera"></div>
  <div class="portrait portrait--b" style="left:154px;top:373px" role="img" aria-label="Contact photo: man in sunglasses with headphones"></div>
</section>

<!-- Screen: Contact list -->
<section class="screen screen--list">
  <header class="app-bar">
    <div class="status-bar">
      <div class="status-bar__left"><span class="signal"><i></i><i></i><i></i><i></i><i></i></span><span>Quorvanet</span></div>
      <span class="status-bar__time">9:23 AM</span>
      <div class="status-bar__right">
        <svg width="8" height="8" viewBox="0 0 8 8"><path d="M7.5.5L.5 3.6l3.2.6.6 3.3z" fill="#fff"/></svg>
        <span>66%</span><span class="battery"></span>
      </div>
    </div>
    <div class="nav">
      <span class="nav__left">
        <svg width="12" height="18" viewBox="0 0 12 18"><path d="M9 2L3 9l6 7" stroke="#fff" stroke-width="2.4" fill="none" stroke-linecap="round" stroke-linejoin="round"/></svg>
      </span>
      <h1 class="nav__title">Contact List</h1>
      <span class="nav__right">
        <svg width="16" height="16" viewBox="0 0 16 16"><path d="M8 1v14M1 8h14" stroke="#fff" stroke-width="2.4" stroke-linecap="round"/></svg>
      </span>
    </div>
  </header>
  <div class="contact-list">
    <div class="contact-row" style="top:60px"><span class="avatar avatar--a" role="img" aria-label="Contact photo"></span>0412-5517308</div>
    <div class="contact-row" style="top:125px"><span class="avatar avatar--b" role="img" aria-label="Contact photo"></span>305-81726490</div>
    <div class="contact-row contact-row--swiped" style="top:190px">
      <div class="row-actions">
        <svg width="16" height="20" viewBox="0 0 16 20"><path d="M1 4h14M6 4V2h4v2M3 4l1 15h8l1-15M6.5 7v9M9.5 7v9" stroke="#fff" stroke-width="1.5" fill="none"/></svg>
        <svg width="20" height="20" viewBox="0 0 20 20"><path d="M3 17l1-4L14 3l3 3L7 16zM12 5l3 3M3 17h14" stroke="#fff" stroke-width="1.5" fill="none" stroke-linejoin="round"/></svg>
      </div>
      <span class="avatar avatar--c" role="img" aria-label="Contact photo"></span>648-20519374
    </div>
    <div class="contact-row" style="top:255px"><span class="avatar avatar--d" role="img" aria-label="Contact photo"></span>3384610-2297</div>
    <div class="contact-row" style="top:320px"><span class="avatar avatar--a" role="img" aria-label="Contact photo"></span>0412-5517308</div>
    <div class="contact-row" style="top:385px"><span class="avatar avatar--b" role="img" aria-label="Contact photo"></span>305-81726490</div>
    <div class="contact-row" style="top:450px"><span class="avatar avatar--d" role="img" aria-label="Contact photo"></span>3384610-2297</div>
  </div>
</section>

<!-- Screen: Add details -->
<section class="screen screen--add">
  <header class="app-bar">
    <div class="status-bar">
      <div class="status-bar__left"><span class="signal"><i></i><i></i><i></i><i></i><i></i></span><span>Quorvanet</span></div>
      <span class="status-bar__time">9:23 AM</span>
      <div class="status-bar__right">
        <svg width="8" height="8" viewBox="0 0 8 8"><path d="M7.5.5L.5 3.6l3.2.6.6 3.3z" fill="#fff"/></svg>
        <span>66%</span><span class="battery"></span>
      </div>
    </div>
    <div class="nav">
      <span class="nav__left">
        <svg width="12" height="18" viewBox="0 0 12 18"><path d="M9 2L3 9l6 7" stroke="#fff" stroke-width="2.4" fill="none" stroke-linecap="round" stroke-linejoin="round"/></svg>
      </span>
      <h1 class="nav__title">Add Details</h1>
      <span class="nav__right">
        <svg width="16" height="14" viewBox="0 0 16 14"><path d="M1.5 7.5l4.5 4.5L14.5 2" stroke="#fff" stroke-width="2.4" fill="none" stroke-linecap="round" stroke-linejoin="round"/></svg>
      </span>
    </div>
  </header>
  <div class="hero">
    <span class="hero__halo"></span>
    <div class="add-image">
      <svg width="46" height="36" viewBox="0 0 46 36"><path fill="#fff" d="M15 2h16l3 5h8a3 3 0 013 3v22a3 3 0 01-3 3H4a3 3 0 01-3-3V10a3 3 0 013-3h8z"/><circle cx="23" cy="20" r="9.5" fill="#4a9fdc"/><circle cx="23" cy="20" r="6.5" fill="#fff"/></svg>
    </div>
    <p class="add-image__label">Add image</p>
  </div>
  <p class="field-label">
    <svg width="12" height="12" viewBox="0 0 24 24"><path fill="#3b93d4" d="M6.6 10.8a15.2 15.2 0 006.6 6.6l2.2-2.2a1 1 0 011-.25 11.4 11.4 0 003.6.57 1 1 0 011 1V20a1 1 0 01-1 1A17 17 0 013 4a1 1 0 011-1h3.5a1 1 0 011 1c0 1.250.2 2.45.57 3.6a1 1 0 01-.25 1z"/></svg>
    Enter Contact Number
  </p>
  <div class="field-input">xxxx-xxxxx-xxxxx</div>
  <footer class="toolbar">
    <svg width="16" height="20" viewBox="0 0 16 20"><path d="M1 4h14M6 4V2h4v2M3 4l1 15h8l1-15M6.5 7v9M9.5 7v9" stroke="#9a9ea3" stroke-width="1.5" fill="none"/></svg>
    <svg width="24" height="20" viewBox="0 0 24 20"><rect x="5" y="1.5" width="17" height="13" fill="none" stroke="#9a9ea3" stroke-width="1.5" transform="rotate(6 13 8)"/><rect x="2" y="5" width="17" height="13" fill="#e9e9eb" stroke="#9a9ea3" stroke-width="1.5"/><path d="M3.5 16.5l5-5 3 3 2-2 4 4z" fill="#9a9ea3"/></svg>
  </footer>
</section>

</body>
</html>
```